BrivoPeak Business Card Design Project

We are looking for a modern, clean business card design for our new company. We are a consulting firm focused on the financial services market providing management and IT consulting to banks, insurance companies, etc. Please include our company logo and company contact information from the attached file in the design. Two versions of the logo are attached, either version is acceptable. Logos are available in other file formats if needed. We would like to include the contact information for both our UK and US offices as well as the following information for each individual card holder: Name, position/title, address, phone number and e-mail address.
Updates
Project Deadline Extended
Reason: A last minute trip over seas has prevented us from finalizing the decision. A decision will be made this week. We apologize for the inconvenience.
Industry/Entity Type
Business
Contact Information for Business Card
Company logo.
Company locations and phone numbers for both the US and UK offices.
Company URL.
Cardholder Name
Cardholder Position/title
Cardholder Address
Cardholder Phone Number
Cardholder e-mail Address
Look and feel
Each slider illustrates characteristics of the customer's brand and the style your logo design should communicate.

```html
<!DOCTYPE html>
<html lang="en">
<head>
<meta charset="utf-8">
<title>BrivoPeak Partners – Business Card</title>
<link rel="stylesheet" href="https://fonts.googleapis.com/css2?family=Open+Sans:wght@400;600;700&display=swap">
<style>
  :root {
    --navy: #17315c;
    --navy-deep: #122a50;
    --grey: #6f7275;
    --grey-light: #9a9c9e;
    --text: #2b2d30;
    --paper: #ffffff;
    --stage: #e9eaec;
  }
  * { box-sizing: border-box; margin: 0; padding: 0; }
  html, body {
    width: 1200px; height: 900px; overflow: hidden;
    background: var(--stage);
    font-family: "Open Sans", Arial, sans-serif;
  }
  .stage {
    width: 1200px; height: 900px;
    display: flex; align-items: center; justify-content: center; gap: 40px;
  }
  .card {
    position: relative;
    width: 540px; height: 309px;
    border-radius: 3px;
    overflow: hidden;
    box-shadow: 0 8px 24px rgba(0,0,0,0.18);
  }

  /* Back side */
  .card-back { background: var(--navy); }
  .card-back .brand {
    position: absolute; right: 40px; top: 60px;
    color: var(--paper); font-weight: 700; text-align: right;
    line-height: 1.1;
  }
  .card-back .brand-name { font-size: 36px; letter-spacing: -0.5px; }
  .card-back .brand-sub { font-size: 14px; letter-spacing: 3px; }

  /* Front side */
  .card-front { background: var(--paper); }
  .card-front .brand {
    position: absolute; left: 30px; top: 104px; width: 220px;
    text-align: center; color: var(--navy); font-weight: 700; line-height: 1.15;
  }
  .card-front .brand-mark {
    display: block; width: 34px; height: 34px; margin: 0 auto 12px;
    border-radius: 50%; background: var(--navy);
  }
  .card-front .brand-name { font-size: 30px; letter-spacing: -0.5px; }
  .card-front .brand-sub { font-size: 12px; letter-spacing: 3px; }

  .divider {
    position: absolute; left: 270px; top: 70px;
    width: 1px; height: 150px;
    background: linear-gradient(to bottom, transparent, var(--navy) 40%, var(--navy) 60%, transparent);
  }
  .holder {
    position: absolute; left: 292px; top: 58px; color: var(--text);
  }
  .holder-name { font-size: 18px; font-weight: 700; color: var(--navy); line-height: 1.1; }
  .holder-title { font-size: 13px; color: var(--grey); margin-bottom: 12px; }
  .address { font-size: 12.5px; line-height: 1.35; margin-bottom: 12px; }
  .contact-list { list-style: none; font-size: 12.5px; line-height: 1.65; }
  .contact-list li { display: flex; align-items: center; gap: 8px; }
  .contact-list svg { width: 11px; height: 11px; fill: var(--navy); flex: none; }
  .contact-list .web { font-size: 13.5px; }

  .card-base { position: absolute; left: 0; bottom: 0; width: 540px; height: 46px; }
</style>
</head>
<body>
<main class="stage">

  <section class="card card-back" aria-label="Business card back">
    <div class="brand">
      <div class="brand-name">BrivoPeak</div>
      <div class="brand-sub">PARTNERS</div>
    </div>
  </section>

  <section class="card card-front" aria-label="Business card front">
    <div class="brand">
      <span class="brand-mark"></span>
      <div class="brand-name">BrivoPeak</div>
      <div class="brand-sub">PARTNERS</div>
    </div>

    <div class="divider"></div>

    <div class="holder">
      <p class="holder-name">Add Name</p>
      <p class="holder-title">Manager</p>
      <p class="address">218 N Cedar Row, Suite 204-210<br>Fairbrook UT 84120<br>United States</p>
      <ul class="contact-list">
        <li>
          <svg viewBox="0 0 24 24" aria-hidden="true"><path d="M6.6 10.8a15.1 15.1 0 0 0 6.6 6.6l2.2-2.2c.3-.3.7-.4 1-.2 1.1.4 2.3.6 3.6.6.6 0 1 .4 1 1V20c0 .6-.4 1-1 1A17 17 0 0 1 3 4c0-.6.4-1 1-1h3.5c.6 0 1 .4 1 1 0 1.3.2 2.5.6 3.6.1.3 0 .7-.2 1z"/></svg>
          (801) 555-0142
        </li>
        <li>
          <svg viewBox="0 0 24 24" aria-hidden="true"><path d="M6.6 10.8a15.1 15.1 0 0 0 6.6 6.6l2.2-2.2c.3-.3.7-.4 1-.2 1.1.4 2.3.6 3.6.6.6 0 1 .4 1 1V20c0 .6-.4 1-1 1A17 17 0 0 1 3 4c0-.6.4-1 1-1h3.5c.6 0 1 .4 1 1 0 1.3.2 2.5.6 3.6.1.3 0 .7-.2 1z"/></svg>
          +44 7700 900418
        </li>
        <li class="web">
          <svg viewBox="0 0 24 24" aria-hidden="true"><path d="M12 2a10 10 0 1 0 0 20 10 10 0 0 0 0-20zm6.9 6h-3a15.7 15.7 0 0 0-1.3-3.9A8 8 0 0 1 18.9 8zM12 4c.8 1.2 1.5 2.5 1.9 4h-3.8c.4-1.5 1.1-2.8 1.9-4zM4.3 14a8 8 0 0 1 0-4h3.4a16.5 16.5 0 0 0 0 4zm.8 2h3a15.7 15.7 0 0 0 1.3 3.9A8 8 0 0 1 5.1 16zm3-8h-3a8 8 0 0 1 4.3-3.9C8.8 5.3 8.4 6.6 8.1 8zM12 20c-.8-1.2-1.5-2.5-1.9-4h3.8c-.4 1.5-1.1 2.8-1.9 4zm2.3-6H9.7a14.7 14.7 0 0 1 0-4h4.6a14.7 14.7 0 0 1 0 4zm.3 5.9c.6-1.2 1-2.5 1.3-3.9h3a8 8 0 0 1-4.3 3.9zM16.3 14a16.5 16.5 0 0 0 0-4h3.4a8 8 0 0 1 0 4z"/></svg>
          www.brivopeakpartners.com
        </li>
      </ul>
    </div>

    <svg class="card-base" viewBox="0 0 540 46" preserveAspectRatio="none" aria-hidden="true">
      <path d="M0 22 H392 C380 30 372 40 366 46 H0 Z" fill="var(--grey-light)"/>
      <path d="M0 30 H384 C378 36 372 42 368 46 H0 Z" fill="var(--grey)"/>
      <path d="M420 14 H540 V46 H386 C396 28 404 14 420 14 Z" fill="var(--navy)"/>
    </svg>
  </section>

</main>
</body>
</html>
```